Letter Head Design

I need a letter head design based on my company logo that I attached.
Include phone number: (403)582-4316
Address: 347 14th Avenue NE, Calgary, Alberta, Canada, T3K 4R8

Industry/Entity Type

It Company

```html
<!DOCTYPE html>
<html lang="en">
<head>
<meta charset="utf-8">
<title>BrightRoom Interiors Corp. Letterhead</title>
<link rel="stylesheet" href="https://fonts.googleapis.com/css2?family=Arimo:wght@400;700&family=Open+Sans:wght@400&display=swap">
<style>
  :root {
    --green: #4fb24a;
    --blue: #1f64b5;
    --blue-dark: #174f9a;
    --ink: #111111;
    --muted: #6d6d6d;
    --paper: #ffffff;
  }
  * { box-sizing: border-box; margin: 0; padding: 0; }
  html, body { width: 927px; height: 1200px; overflow: hidden; background: var(--paper); }
  .letterhead {
    position: relative;
    width: 927px;
    height: 1200px;
    background: var(--paper);
    font-family: "Arimo", Arial, sans-serif;
    color: var(--ink);
    overflow: hidden;
  }
  .header-wave { position: absolute; top: 0; left: 0; width: 927px; height: 170px; }
  .brand {
    position: absolute;
    left: 60px;
    top: 120px;
    width: 220px;
  }
  .brand-mark {
    display: block;
    width: 110px;
    height: 110px;
    margin-left: 52px;
    background: var(--green);
    border-radius: 6px;
  }
  .brand-name {
    display: block;
    margin-top: 14px;
    font-family: "Arimo", Arial, sans-serif;
    font-weight: 700;
    font-size: 36px;
    line-height: 1;
    color: var(--blue);
    letter-spacing: -0.5px;
    white-space: nowrap;
  }
  .letter {
    position: absolute;
    left: 109px;
    top: 357px;
    width: 715px;
    font-size: 19px;
    line-height: 27px;
  }
  .letter-date { margin-bottom: 34px; }
  .letter-salutation { margin-bottom: 27px; }
  .letter-salutation strong { font-weight: 700; }
  .letter-body p { margin-bottom: 27px; }
  .footer-band { position: absolute; left: 0; bottom: 0; width: 927px; height: 100px; }
  .footer-contact {
    position: absolute;
    left: 64px;
    top: 1152px;
    font-family: "Open Sans", Arial, sans-serif;
    font-size: 14.5px;
    color: var(--muted);
    white-space: nowrap;
  }
  .footer-contact .divider { color: var(--ink); margin: 0 6px; }
  .footer-brand {
    position: absolute;
    left: 690px;
    top: 1127px;
    display: flex;
    align-items: center;
    gap: 14px;
  }
  .footer-brand-mark {
    width: 52px;
    height: 52px;
    background: var(--paper);
    border-radius: 4px;
  }
  .footer-brand-name {
    font-family: "Arimo", Arial, sans-serif;
    font-weight: 700;
    font-size: 25px;
    color: var(--paper);
    white-space: nowrap;
  }
</style>
</head>
<body>
<div class="letterhead">
  <svg class="header-wave" viewBox="0 0 927 170" aria-hidden="true">
    <path d="M0 0 H927 V162 C850 168 720 150 560 118 C380 80 200 38 0 60 Z" fill="var(--blue)"/>
    <path d="M0 0 H927 V138 C850 146 720 128 560 96 C380 58 200 20 0 38 Z" fill="var(--green)"/>
    <path d="M0 40 C200 22 380 60 560 98 C720 130 850 148 927 140" fill="none" stroke="var(--paper)" stroke-width="5"/>
  </svg>

  <div class="brand">
    <span class="brand-mark"></span>
    <span class="brand-name">BrightRoom</span>
  </div>

  <main class="letter">
    <p class="letter-date">April 16, 2014</p>
    <p class="letter-salutation"><strong>Mr. Paul Weston</strong>,</p>
    <div class="letter-body">
      <p>Lorem ipsum dolor sit amet, consectetur adipiscing elit. Morbi vel ultrices nisl. Ut porttitor accumsan ipsum, quis gravida elit commodo sed. Vivamus pharetra tincidunt mauris. Donec vestibulum mi at diam viverra volutpat. Donec auctor non orci semper porta. Praesent neque erat, tincidunt ut elementum adipiscing, pulvinar eu diam. In hac habitasse platea dictumst. Praesent euismod arcu risus, nec vulputate libero aliquam et. Nam pretium nisi sed orci molestie aliquam. Integer dolor urna, interdum ac ligula a, facilisis interdum lacus.</p>
      <p>Sed sodales non lacus venenatis eleifend. Aliquam erat volutpat. Integer mattis sapien a quam consequat, eu elementum leo tincidunt. Proin in nunc auctor, pellentesque nisl eu, ullamcorper neque. Duis eget euismod ligula. Nunc rhoncus justo ut odio adipiscing malesuada. Vivamus sagittis lacus id velit pharetra molestie. Aliquam placerat sodales purus, vel interdum ipsum faucibus elementum. Class aptent taciti sociosqu ad litora torquent per conubia nostra, per inceptos himenaeos. Curabitur faucibus massa ligula, ut laoreet nulla mattis id. Suspendisse ipsum arcu, pharetra id interdum nec, sagittis non metus.</p>
    </div>
    <p class="letter-closing">Sincerely,<br>Bright Room | Interiors Corp.</p>
  </main>

  <svg class="footer-band" viewBox="0 0 927 100" aria-hidden="true">
    <path d="M607 100 L680 8 H927 V100 Z" fill="var(--blue)"/>
    <rect x="0" y="93" width="927" height="7" fill="var(--blue-dark)"/>
  </svg>

  <p class="footer-contact">(403)582-4316<span class="divider">|</span>347 14th Avenue NE, Calgary, Alberta, Canada, T3K 4R8</p>

  <div class="footer-brand">
    <span class="footer-brand-mark"></span>
    <span class="footer-brand-name">BrightRoom</span>
  </div>
</div>
</body>
</html>
```